Redesign of Smart Watch Gift Voucher-SEE ATTACHED CURRENT DESIGN

I need to redesign my existing design using all same content and elements.

MY ENVISION: I invision more of a professional advertisement type of flyer/voucher. Imagine how Corvel.com would create a professionally looking flyer promoting the lumo or veno.

you can get many ideas about professional design by looking at some of corvels flyer designs :
https://www.findora-example.net/search?q=lumo+advertisment&mode=img&ref=a83kd02mzq7

stock photos are attached, you do not have to use them all, you can use some or none i am open to your designs using your own images if you want...just make sure the smartwatch looks black

DO NOT LEAVE ANY CONTENT OR ELEMENTS OUT ON MOCK UP PLEASE

SEE ATTACHED CURRENT DESIGN

I need to redesign my existing design using all same content and elements. DO NOT LEAVE ANY CONTENT OR ELEMENTS OUT ON MOCK UP PLEASE

Target Market(s)

B2B-you can get many ideas about professional design by looking at some of corvels flyer designs :

Industry/Entity Type

Marketing

Requirements
Must have
• I need to redesign my existing design using all same content and elements. DO NOT LEAVE ANY CONTENT OR ELEMENTS OUT ON MOCK UP PLEASE

Nice to have

Should not have

```html
<!DOCTYPE html>
<html lang="en">
<head>
<meta charset="utf-8">
<title>Smartwatch Gift Voucher Flyer</title>
<link rel="stylesheet" href="https://fonts.googleapis.com/css2?family=Montserrat:wght@600;700;800;900&family=Open+Sans:wght@400;600;700&display=swap">
<style>
  :root {
    --red: #d3202a;
    --red-dark: #a8141c;
    --ink: #2b2b2b;
    --muted: #5d5d5d;
    --paper: #ffffff;
    --band: #eeeeee;
    --photo-light: #e9eef3;
    --photo-mid: #b9c7d6;
    --shirt: #3f74b8;
  }
  * { box-sizing: border-box; margin: 0; padding: 0; }
  html, body { width: 887px; height: 1200px; overflow: hidden; background: var(--paper); }
  body { font-family: "Open Sans", Arial, sans-serif; color: var(--ink); }

  .flyer { position: relative; width: 887px; height: 1200px; overflow: hidden; background: var(--paper); }

  .hero-photo {
    position: absolute; left: 0; top: 0; width: 887px; height: 500px;
    background:
      radial-gradient(ellipse 260px 200px at 38% 62%, var(--shirt) 0%, rgba(63,116,184,0) 100%),
      linear-gradient(160deg, var(--photo-light) 0%, #dde4ec 55%, var(--photo-mid) 100%);
  }
  .hero-curve { position: absolute; left: 0; top: 360px; width: 887px; height: 180px; }

  .content { position: absolute; left: 58px; top: 512px; width: 770px; }
  .intro { font-size: 15px; line-height: 1.55; color: var(--muted); margin-bottom: 16px; }
  .section-title {
    font-family: "Montserrat", Arial, sans-serif; font-weight: 800; font-size: 19px;
    color: var(--red); letter-spacing: .5px; margin-bottom: 8px;
  }
  .body-text { font-size: 15px; line-height: 1.55; color: var(--muted); margin-bottom: 16px; }

  .feature-list {
    list-style: none; display: grid; grid-template-columns: repeat(3, 1fr);
    row-gap: 8px; column-gap: 20px; margin-bottom: 22px; width: 720px;
  }
  .feature-list li { font-size: 14px; font-weight: 600; color: var(--ink); display: flex; align-items: center; }
  .feature-list li::before {
    content: ""; width: 9px; height: 9px; background: var(--red); margin-right: 10px; flex: none;
  }

  .voucher { width: 420px; }
  .voucher-title { font-size: 17px; }
  .voucher p { font-size: 14px; line-height: 1.5; color: var(--muted); }
  .voucher .code { font-weight: 700; color: var(--ink); margin-top: 6px; }
  .voucher .web { font-family: "Montserrat", Arial, sans-serif; font-weight: 700; font-size: 17px; color: var(--ink); margin: 4px 0; }
  .voucher .small { font-size: 12px; }

  .promo { position: absolute; left: 537px; top: 830px; width: 520px; height: 520px; }
  .promo-disc { position: absolute; inset: 0; border-radius: 50%; background: var(--red); }
  .watch-photo {
    position: absolute; left: 70px; top: 28px; width: 124px; height: 124px; border-radius: 50%;
    background: radial-gradient(circle at 50% 50%, #1b1b1b 0 30%, #6a6a6a 62%, #c9c9c9 100%);
    border: 5px solid var(--paper);
  }
  .promo-text { position: absolute; left: 30px; top: 162px; width: 300px; color: var(--paper); text-align: right; }
  .promo-text .enjoy { font-family: "Montserrat", Arial, sans-serif; font-weight: 900; font-size: 56px; line-height: 1; letter-spacing: 1px; }
  .promo-text .line { font-family: "Montserrat", Arial, sans-serif; font-weight: 700; font-size: 21px; line-height: 1.1; }
  .promo-text .tag { font-size: 13px; margin-top: 6px; line-height: 1.35; }

  .footer-band {
    position: absolute; left: 0; bottom: 0; width: 887px; height: 46px; background: var(--band);
    display: flex; align-items: center; gap: 60px; padding-left: 58px;
    font-family: "Montserrat", Arial, sans-serif; font-size: 12px; font-weight: 700; color: var(--ink); letter-spacing: .5px;
  }
</style>
</head>
<body>
<main class="flyer">
  <div class="hero-photo" role="img" aria-label="Photo of a man in a blue shirt checking the black smartwatch on his wrist, surrounded by fitness feature icons"></div>

  <svg class="hero-curve" viewBox="0 0 887 180" preserveAspectRatio="none" aria-hidden="true">
    <path d="M0 40 C 260 150, 620 160, 887 90 L887 180 L0 180 Z" fill="#ffffff"/>
    <path d="M0 40 C 260 150, 620 160, 887 90" fill="none" stroke="#d3202a" stroke-width="6"/>
  </svg>

  <section class="content">
    <p class="intro">Congratulations, you have been selected with a Brand New Smart Watch. Simply register below and we will ship your watch to your door with free delivery. There is no catch, only a small card fee. Your new watch helps you track health, steps, sleep and messages every single day.</p>

    <h2 class="section-title">HOW CAN WE DO THIS</h2>
    <p class="body-text">We have a simple retail partnership that lets us send a limited number of watches to loyal customers at no cost. Our partners cover the watch itself, you only cover the postage. Stock is limited, so claim yours today.</p>

    <ul class="feature-list">
      <li>Heart Rate Monitor</li>
      <li>Blood Pressure Monitor</li>
      <li>Long Battery Life</li>
      <li>Step Counter</li>
      <li>Calorie Counter</li>
      <li>Free Shipping</li>
      <li>Sleep Tracking</li>
      <li>Water Resistant</li>
      <li>Camera Remote</li>
      <li>Message Alerts</li>
      <li>Music Control</li>
      <li>Call Notifications</li>
    </ul>

    <div class="voucher">
      <h3 class="section-title voucher-title">YOUR VOUCHER</h3>
      <p>Visit our website below and enter your voucher code to claim your free smartwatch today.</p>
      <p class="code">Voucher Code: RW-4821</p>
      <p class="web">www.rewardsdirect-example.com</p>
      <p class="small">Offer valid while stock lasts, one per household.</p>
    </div>
  </section>

  <aside class="promo">
    <div class="promo-disc"></div>
    <div class="watch-photo" role="img" aria-label="Close-up photo of the black smartwatch on a wrist"></div>
    <div class="promo-text">
      <div class="enjoy">ENJOY</div>
      <div class="line">YOUR BRAND NEW</div>
      <div class="line">SMARTWATCH</div>
      <p class="tag">Take control of your life with<br>your new smart fitness watch</p>
    </div>
  </aside>

  <footer class="footer-band">
    <span>CERTIFICATE ID: 0042187</span>
    <span>EXPIRES: 30/11/2025</span>
  </footer>
</main>
</body>
</html>
```